Financial Services Postcard Design

Lionel Budwig, CPA
Financial Services
Accounting/Tax/Consulting
Services include but not limited to
Financial Statements
Tax Returns
CFO/Controller services
Budgeting and Forecasting
Cash Management
Payroll / AP/ AR
Insurance Analysis
Cost Analysis
Special projects

I need a postcard design for my new financial service company to assist businesses in the Orange County area of southern California. I'm looking for a warm but bright look to represent CPA with many years of Management experience with manufacturing companies that can relate to business issues and provide solutions for small business.

```html
<!DOCTYPE html>
<html lang="en">
<head>
<meta charset="utf-8">
<title>Lionel Budwig, CPA – Financial Services Postcard</title>
<link href="https://fonts.googleapis.com/css2?family=Arimo:wght@400;700&display=swap" rel="stylesheet">
<style>
  :root {
    --green-dark: #0f6a1c;
    --green-mid: #1f8a2a;
    --accent-green: #2e9b2e;
    --text-dark: #1a1a1a;
    --white: #ffffff;
    --bg-light: #f4f5f6;
    --bg-grey: #d9dcdf;
    --chart-silver: #c4c8cc;
    --chart-gold: #e2c25a;
  }
  * { margin: 0; padding: 0; box-sizing: border-box; }
  html, body { width: 1200px; height: 863px; overflow: hidden; background: var(--white); }
  body { font-family: "Arimo", Arial, sans-serif; }

  .postcard { position: relative; width: 1200px; height: 863px; overflow: hidden; background: var(--white); }

  .backdrop {
    position: absolute; inset: 0;
    background: radial-gradient(ellipse at 65% 40%, var(--white) 0%, var(--bg-light) 55%, var(--bg-grey) 100%);
  }

  .side-panel {
    position: absolute; left: 51px; top: 0; width: 323px; height: 863px;
    background: linear-gradient(180deg, var(--green-mid) 0%, var(--green-dark) 100%);
  }

  .portrait {
    position: absolute; left: 37px; top: 44px; width: 258px; height: 337px;
    border: 3px solid var(--white);
    background: linear-gradient(180deg, #e9ebee 0%, #c9cdd2 45%, #2a2f3a 100%);
  }

  .contact { position: absolute; left: 37px; top: 398px; color: var(--white); }
  .contact .name { font-weight: 700; font-size: 25px; line-height: 30px; }
  .contact .address { font-size: 20px; line-height: 28px; margin-top: 2px; }
  .contact .phone { font-weight: 700; font-size: 25px; line-height: 30px; margin-top: 30px; }
  .contact .email { font-size: 20px; line-height: 28px; }

  .growth-illustration {
    position: absolute; left: 410px; top: 395px; width: 725px; height: 435px;
    background: linear-gradient(100deg, rgba(196,200,204,0.15) 0%, rgba(196,200,204,0.55) 60%, rgba(226,194,90,0.7) 100%);
    border-radius: 4px;
  }

  .services {
    position: absolute; left: 455px; top: 93px; list-style: none;
    font-size: 26px; line-height: 37.6px; color: var(--text-dark);
  }
  .services li { position: relative; padding-left: 29px; }
  .services li::before {
    content: ""; position: absolute; left: 2px; top: 14px;
    width: 10px; height: 10px; border-radius: 50%; background: var(--accent-green);
  }
  .services .title { color: var(--accent-green); font-weight: 700; }
  .services .title::before {
    width: 10px; height: 10px; border-radius: 0; background: none;
    border-right: 3px solid var(--green-dark); border-top: 3px solid var(--green-dark);
    transform: rotate(45deg); left: -2px; top: 13px;
  }
</style>
</head>
<body>
<main class="postcard">
  <div class="backdrop" role="img" aria-label="Soft grey photo of modern office architecture"></div>

  <aside class="side-panel">
    <div class="portrait" role="img" aria-label="Portrait photo of Lionel Budwig in a suit"></div>
    <div class="contact">
      <p class="name">Lionel Budwig, CPA</p>
      <p class="address">187 N Maplecrest Ln.<br>Anaheim Hills, Ca. 92807</p>
      <p class="phone">714-555-0142</p>
      <p class="email">LBudwig@ledgerline.net</p>
    </div>
  </aside>

  <div class="growth-illustration" role="img" aria-label="Illustration of rising silver bars ending in a gold bar, with a green arrow climbing upward"></div>

  <ul class="services">
    <li class="title">Lionel Budwig, CPA</li>
    <li>Financial Services</li>
    <li>Accounting/Tax/Consulting</li>
    <li>Services include but not limited to</li>
    <li>Financial Statements</li>
    <li>Tax Returns</li>
    <li>CFO/Controller services</li>
    <li>Budgeting and Forecasting</li>
    <li>Cash Management</li>
    <li>Payroll / AP/ AR</li>
    <li>Insurance Analysis</li>
    <li>Cost Analysis</li>
    <li>Special projects</li>
  </ul>
</main>
</body>
</html>
```